CustomerPath UX Overhaul - redesign to improve visitor journeys and conversions

I need my website brought to life, professional and engaging.
I can supply as much pictures as needed to create enhancing visuals. I need your team to review the website and create a list of ideas of what you need from me to bring this vision to life.
The company does 3d modeling, 3d printing with FDM and resin printers, CAD design, 3d scanning.
My website is https://qtforgeworks.com/
Please review it and give me your best.
Target Market(s)
cosplayer, filmmakers, life size prints, custom designs, redesign and scanning, large and small scale prints, replicating
Industry/Entity Type
CAD Design, Additive Manufacturing, 3D Printing, 3D Scanning
Coding
Coded - Design and coding required
Number of Pages Required
3 page
Requirements
Must have
- Professional and clean look, inviting, eye grabber

```html
<!DOCTYPE html>
<html lang="en">
<head>
<meta charset="utf-8">
<title>QT Forgeworks – 3D Printing & Design</title>
<link href="https://fonts.googleapis.com/css2?family=Nunito+Sans:wght@400;600;700;800&display=swap" rel="stylesheet">
<style>
:root{
  --navy:#1c1f63;
  --navy-deep:#16195a;
  --sky:#1ab8ea;
  --sky-btn:#1fb0ea;
  --cta:#3fc6ee;
  --pale:#e9f5fb;
  --foot:#d9f1fb;
  --ink:#222;
  --muted:#666;
  --white:#fff;
}
*{box-sizing:border-box;margin:0;padding:0}
html,body{width:1200px;height:4421px;overflow:hidden}
body{font-family:"Nunito Sans",Arial,sans-serif;color:var(--ink);background:var(--white);position:relative}
section,header,footer{position:relative;width:1200px}
.abs{position:absolute}
.btn{display:inline-block;font-weight:600;font-size:15px;border-radius:3px;text-decoration:none}

.topbar{height:34px;background:#fff;display:flex;align-items:center;padding:0 52px;font-size:14px;gap:20px}
.topbar span{display:flex;align-items:center;gap:6px}
.topbar .social{margin-left:auto;display:flex;gap:10px}
.topbar .social i{display:block;width:26px;height:26px;border:2px solid var(--navy);border-radius:4px}

.nav{height:76px;background:var(--navy);display:flex;align-items:center;padding:0 52px;color:#fff}
.brand{display:flex;align-items:center;gap:8px;font-size:13px;font-weight:700;letter-spacing:1px}
.brand i{width:14px;height:14px;background:var(--sky);display:block}
.nav ul{list-style:none;display:flex;gap:42px;margin-left:auto;font-size:14px;align-items:center}
.nav li.active{color:var(--sky)}

.hero{height:690px;background:linear-gradient(100deg,#2a2f86 0%,#3a4aa0 30%,#5e6bbf 45%,#7fae9a 62%,#b7c55a 80%,#8a8f4a 100%);clip-path:polygon(0 0,100% 0,100% 620px,50% 690px,0 620px)}
.hero::after{content:"";position:absolute;inset:0;background:linear-gradient(90deg,rgba(28,31,99,.85),rgba(28,31,99,.35) 60%,rgba(28,31,99,.15))}
.hero .copy{position:absolute;left:51px;top:128px;z-index:1;color:#fff}
.hero h1{font-size:50px;line-height:60px;font-weight:700;width:920px}
.hero p{font-size:19px;margin-top:30px}
.hero .btn{margin-top:30px;background:#fff;color:var(--navy);padding:11px 22px;font-size:14px;font-weight:700}
.hero-dot{position:absolute;left:572px;top:760px;width:56px;height:56px;border-radius:50%;background:var(--navy);border:3px solid var(--sky);z-index:2}

.section-title{text-align:center;color:var(--navy);font-size:44px;font-weight:700}
.offerings{height:657px}
.offerings .section-title{position:absolute;top:866px;width:100%;top:76px}
.cards{position:absolute;top:153px;left:51px;display:flex;gap:28px}
.card{width:254px;height:437px;position:relative;text-align:center;border:1px solid #8b90b8;border-bottom:none}
.card .photo{height:238px;margin:0}
.card h3{font-size:22px;font-weight:400;margin-top:20px;color:var(--ink)}
.card p{font-size:13px;line-height:21px;padding:0 20px;margin-top:10px}
.card .btn{margin-top:16px;background:var(--navy);color:#fff;padding:7px 22px;font-size:14px;font-weight:400}
.card svg{position:absolute;left:-1px;bottom:-20px}

.about{height:476px;background:var(--pale)}
.about .photo{position:absolute;left:51px;top:38px;width:361px;height:404px;clip-path:polygon(50% 0,100% 25%,100% 75%,50% 100%,0 75%,0 25%);background:linear-gradient(135deg,#8a9bb0,#c9b8a6 55%,#6f7d8c)}
.about .text{position:absolute;left:494px;top:95px;width:630px}
.about h2{font-size:38px;line-height:43px;color:var(--navy);font-weight:700}
.about h4{font-size:22px;font-weight:400;margin-top:18px;display:flex;align-items:center;gap:10px}
.about h4 i{width:32px;height:32px;border-radius:50%;background:radial-gradient(circle,#fff 20%,var(--sky) 22%,var(--navy) 70%);display:block}
.about p{font-size:14px;line-height:27px;color:var(--muted);margin-top:18px}

.featured{height:596px}
.featured .section-title{position:absolute;top:50px;width:100%}
.arrows{position:absolute;right:52px;top:55px;display:flex;gap:10px}
.arrows span{width:45px;height:32px;display:flex;align-items:center;justify-content:center;border:1px solid var(--sky)}
.arrows span.on{background:var(--navy)}
.products{position:absolute;top:132px;left:51px;display:flex;gap:27px}
.product{width:254px;height:423px;box-shadow:0 1px 5px rgba(0,0,0,.18)}
.product .photo{height:245px}
.product h3{font-size:20px;font-weight:400;line-height:24px;padding:0 16px;margin-top:20px;height:48px}
.product .price{font-size:19px;padding:0 16px;margin-top:8px}
.product .btn{margin:20px 0 0 16px;background:var(--sky-btn);color:#fff;padding:7px 20px;font-weight:400;font-size:14px}

.journey{height:478px}
.journey .section-title{position:absolute;top:48px;width:100%}
.journey .sub{position:absolute;top:112px;width:100%;text-align:center;font-size:18px}
.gallery .photo{position:absolute;top:181px;height:256px}
.round{position:absolute;top:292px;width:34px;height:34px;border-radius:50%;background:#fff;border:1px solid #333;display:flex;align-items:center;justify-content:center}

.cta{height:515px;background:var(--cta);clip-path:polygon(0 40px,50% 0,100% 40px,100% 100%,0 100%);text-align:center;color:#fff}
.cta h2{position:absolute;top:100px;width:100%;font-size:44px;color:var(--navy);font-weight:700}
.cta p{position:absolute;top:196px;left:260px;width:680px;font-size:26px;line-height:31px;font-weight:400}
.cta .btn{position:absolute;left:520px;top:332px;background:var(--navy);color:#fff;padding:10px 24px;font-size:16px;font-weight:400}

.contact{height:563px;background:var(--navy);color:#fff}
.contact h2{position:absolute;left:51px;top:28px;font-size:44px;font-weight:700}
.contact .lead{position:absolute;left:52px;top:90px;color:var(--sky);font-size:16px}
.contact .intro{position:absolute;left:52px;top:122px;font-size:14px;line-height:23px;width:420px}
.info{position:absolute;left:52px;display:flex;align-items:center;gap:14px;font-size:14px}
.info i{width:52px;height:52px;border:2px solid #fff;border-radius:50%;display:flex;align-items:center;justify-content:center;background:#fff}
.hours{position:absolute;left:370px;top:255px;font-size:14px;line-height:31px}
.hours b{color:var(--sky);font-weight:400;display:block;line-height:22px}
.form{position:absolute;left:680px;top:86px;width:445px;height:317px;background:var(--sky);padding:30px 24px}
.field{background:#fff;height:38px;border-radius:3px;font-size:12px;padding:10px 14px;margin-bottom:14px;color:var(--ink)}
.field.msg{height:80px}
.form .attach{font-size:12px;margin-top:4px;color:var(--navy)}
.form .btn{margin-top:12px;background:var(--navy);color:#fff;padding:6px 26px;font-size:13px;font-weight:400}

.footer{height:326px;background:var(--foot);color:var(--navy)}
.footer .brand{position:absolute;left:52px;top:110px;color:var(--navy);font-size:18px;font-weight:400;letter-spacing:2px}
.fcol{position:absolute;top:38px;font-size:14px;line-height:30px}
.fcol h5{font-size:15px;font-weight:400;border-bottom:2px solid var(--navy);display:inline-block;line-height:22px;margin-bottom:4px}
.fcol ul{list-style:none}
.fcol.right{right:52px;text-align:right;width:220px}
.fcol.right p{line-height:20px;font-size:13px}
.fcol .email{margin-top:14px;background:#fff;height:38px;line-height:38px;text-align:center;font-size:13px;width:200px;margin-left:auto}
.fcol .btn{margin-top:16px;background:var(--navy);color:#fff;padding:4px 24px;font-size:13px;font-weight:400;line-height:24px;margin-right:42px}
.copyright{position:absolute;bottom:20px;width:100%;text-align:center;font-size:12px;border-top:1px solid #b8dcea;padding-top:14px}
</style>
</head>
<body>

<div class="topbar">
  <span><svg width="22" height="16" viewBox="0 0 22 16"><rect x="1" y="1" width="20" height="14" fill="none" stroke="#1c1f63" stroke-width="1.5"/><path d="M1 1l10 8 10-8" fill="none" stroke="#1c1f63" stroke-width="1.5"/></svg>info@qtforgeworks.com</span>
  <span><svg width="20" height="20" viewBox="0 0 24 24"><path d="M5 3h4l2 5-3 2a12 12 0 0 0 6 6l2-3 5 2v4a2 2 0 0 1-2 2A18 18 0 0 1 3 5a2 2 0 0 1 2-2z" fill="none" stroke="#1c1f63" stroke-width="1.5"/></svg>55501230199</span>
  <div class="social"><i></i><i></i></div>
</div>

<header class="nav">
  <div class="brand"><i></i>QT FORGEWORKS</div>
  <ul>
    <li class="active">Home</li><li>About</li><li>Services</li><li>Featured Product</li><li>Contact Us</li>
    <li><svg width="30" height="30" viewBox="0 0 30 30"><circle cx="15" cy="15" r="13" fill="none" stroke="#1ab8ea" stroke-width="2"/><circle cx="15" cy="12" r="5" fill="none" stroke="#1ab8ea" stroke-width="2"/><path d="M6 24c3-5 15-5 18 0" fill="none" stroke="#1ab8ea" stroke-width="2"/></svg></li>
  </ul>
</header>

<section class="hero" role="img" aria-label="Large colourful 3D printed figures with cartoon eyes in a print lab">
  <div class="copy">
    <h1>PRECISION 3D PRINTING &amp; DESIGN SERVICES - PERSONALIZED PRODUCTS &amp; SOLUTIONS</h1>
    <p>TRANSFORMING IDEAS INTO REALITY, ONE LAYER AT A TIME.</p>
    <a class="btn">GET A QUOTE</a>
  </div>
</section>
<div class="hero-dot" style="top:760px"></div>

<section class="offerings">
  <h2 class="section-title">OUR OFFERINGS</h2>
  <div class="cards">
    <div class="card"><div class="photo" role="img" aria-label="3D printed superhero figure" style="background:linear-gradient(160deg,#4c5568,#2b3350 60%,#9aa0ad)"></div><h3>3D Modling</h3><p>Lorem Ipsum is simply dummy text of the printing and typeset­ting industry.</p><a class="btn">Read More</a><svg width="256" height="22"><polyline points="0,0 128,20 256,0" fill="none" stroke="#8b90b8"/></svg></div>
    <div class="card"><div class="photo" role="img" aria-label="Red 3D printed woven basket" style="background:linear-gradient(160deg,#20305e,#b5353f 55%,#6a2a38)"></div><h3>3D Printing with FDM</h3><p>Lorem Ipsum is simply dummy text of the printing and typeset­ting industry.</p><a class="btn">Read More</a><svg width="256" height="22"><polyline points="0,0 128,20 256,0" fill="none" stroke="#8b90b8"/></svg></div>
    <div class="card"><div class="photo" role="img" aria-label="Rainbow striped spiral egg model" style="background:linear-gradient(160deg,#2a2a2a,#e8c77a 40%,#8fc6d9 60%,#333)"></div><h3>CAD Design</h3><p>Lorem Ipsum is simply dummy text of the printing and typeset­ting industry.</p><a class="btn">Read More</a><svg width="256" height="22"><polyline points="0,0 128,20 256,0" fill="none" stroke="#8b90b8"/></svg></div>
    <div class="card"><div class="photo" role="img" aria-label="Inside of a 3D printer build chamber" style="background:linear-gradient(160deg,#3a3d42,#8b9096 50%,#2e3135)"></div><h3>3D Scanning</h3><p>Lorem Ipsum is simply dummy text of the printing and typeset­ting industry.</p><a class="btn">Read More</a><svg width="256" height="22"><polyline points="0,0 128,20 256,0" fill="none" stroke="#8b90b8"/></svg></div>
  </div>
</section>

<section class="about">
  <div class="photo" role="img" aria-label="Team working together at 3D printers in a workshop"></div>
  <div class="text">
    <h2>ABOUT QT<br>FORGEWORKS</h2>
    <h4><i></i>Our Mission</h4>
    <p>At QT Forgeworks, our mission is to turn visions into reality, layer by layer. As a small family-owned business based in Connecticut, we are dedicated to providing high-quality 3D printing and engraving services for all kinds of projects.</p>
  </div>
</section>

<section class="featured">
  <h2 class="section-title">FEATURED PRODUCTS</h2>
  <div class="arrows">
    <span><svg width="12" height="16"><polyline points="9,2 3,8 9,14" fill="none" stroke="#1c1f63" stroke-width="2"/></svg></span>
    <span class="on"><svg width="12" height="16"><polyline points="3,2 9,8 3,14" fill="none" stroke="#fff" stroke-width="2"/></svg></span>
  </div>
  <div class="products">
    <div class="product"><div class="photo" role="img" aria-label="Metallic bullet-shaped storage containers" style="background:linear-gradient(90deg,#c87a2a,#9aa6b0 35%,#8a2a2a 60%,#d8a23a)"></div><h3>Bullet Replica Storage Containers</h3><div class="price">$45.95</div><a class="btn">Shop Now</a></div>
    <div class="product"><div class="photo" role="img" aria-label="Glowing motorcycle shop LED sign" style="background:radial-gradient(circle,#b02020,#5a0f0f 60%,#111)"></div><h3>Vintage Motorcycle RGB LED Sign</h3><div class="price">$45.95</div><a class="btn">Shop Now</a></div>
    <div class="product"><div class="photo" role="img" aria-label="Egg resting in a white egg cracker on granite" style="background:linear-gradient(140deg,#6a5e52,#d7a88a 45%,#e8e6e2 65%,#5a5048)"></div><h3>Egg-Shaped Egg Cracker</h3><div class="price">$45.95</div><a class="btn">Shop Now</a></div>
    <div class="product"><div class="photo" role="img" aria-label="Copper coloured nut-shaped storage container" style="background:linear-gradient(140deg,#3c5a86,#b8743a 50%,#d9d9d9)"></div><h3>Multi-Size Electrical Nut Storage Container</h3><div class="price">$45.95</div><a class="btn">Shop Now</a></div>
  </div>
</section>

<section class="journey">
  <h2 class="section-title">EXPLORE OUR CREATIVE JOURNEY</h2>
  <div class="sub">A SHOWCASE OF 3D PRINTING AND DESIGN PROJECTS</div>
  <div class="gallery">
    <div class="photo" role="img" aria-label="Designers working at a 3D printer" style="left:0;width:398px;background:linear-gradient(120deg,#8d98a6,#c9b9a8 50%,#5f6e80)"></div>
    <div class="photo" role="img" aria-label="Printer nozzle laying blue filament" style="left:426px;width:347px;background:linear-gradient(160deg,#9aa3ab,#c46b3a 55%,#3a7ad0)"></div>
    <div class="photo" role="img" aria-label="Yellow part being printed" style="left:802px;width:398px;background:linear-gradient(160deg,#d9c7a0,#6d6050 45%,#f3c313)"></div>
  </div>
  <div class="round" style="left:53px"><svg width="16" height="14"><path d="M15 7H2M7 2L2 7l5 5" fill="none" stroke="#222" stroke-width="1.6"/></svg></div>
  <div class="round" style="left:1113px"><svg width="16" height="14"><path d="M1 7h13M9 2l5 5-5 5" fill="none" stroke="#222" stroke-width="1.6"/></svg></div>
</section>

<section class="cta">
  <h2>EXPLORE OUR CREATIVE JOURNEY</h2>
  <p>Discover expert 3D printing and engraving services. We turn your visions into reality, supporting veterans along the way!</p>
  <a class="btn">Pay Now</a>
</section>

<section class="contact">
  <h2>CONTACT US</h2>
  <div class="lead">We're always available to talk dreams!</div>
  <div class="intro">We value our customers and are always ready to listen, collaborate, and create personalized products together.</div>
  <div class="info" style="top:270px"><i><svg width="22" height="26" viewBox="0 0 22 26"><path d="M11 25S2 15 2 9a9 9 0 0 1 18 0c0 6-9 16-9 16z" fill="none" stroke="#1c1f63" stroke-width="1.6"/><circle cx="11" cy="9" r="3" fill="none" stroke="#1c1f63" stroke-width="1.6"/></svg></i>Harbor Falls CT 06999</div>
  <div class="info" style="top:340px"><i><svg width="24" height="24" viewBox="0 0 24 24"><path d="M5 3h4l2 5-3 2a12 12 0 0 0 6 6l2-3 5 2v4a2 2 0 0 1-2 2A18 18 0 0 1 3 5a2 2 0 0 1 2-2z" fill="none" stroke="#1c1f63" stroke-width="1.6"/></svg></i>1 (555) 010.4477</div>
  <div class="info" style="top:410px"><i><svg width="26" height="18" viewBox="0 0 26 18"><rect x="1" y="1" width="24" height="16" fill="none" stroke="#1c1f63" stroke-width="1.6"/><path d="M1 1l12 9 12-9" fill="none" stroke="#1c1f63" stroke-width="1.6"/></svg></i>info@qtforgeworks.com</div>
  <div class="hours">
    <b>Hours</b>
    Mon&nbsp; 09:00 am – 05:00 pm<br>Tue&nbsp;&nbsp; 09:00 am – 05:00 pm<br>Wed 09:00 am – 05:00 pm<br>Thu&nbsp;&nbsp; 09:00 am – 05:00 pm<br>Fri&nbsp;&nbsp;&nbsp;&nbsp; 09:00 am – 05:00 pm<br>Sat&nbsp; Closed<br>Sun Closed
  </div>
  <div class="form">
    <div class="field">Name</div>
    <div class="field">E Mail*</div>
    <div class="field msg">Message</div>
    <div class="attach">&#128206; Attach Files</div>
    <a class="btn">Send Now</a>
  </div>
</section>

<footer class="footer">
  <div class="brand"><i></i>QT FORGEWORKS</div>
  <div class="fcol" style="left:426px"><h5>Navigation</h5><ul><li>Home</li><li>About</li><li>Services</li><li>Featured Product</li><li>Contact Us</li></ul></div>
  <div class="fcol" style="left:708px"><h5>What we do</h5><ul><li>3D Modeling</li><li>3D Printing with FDM</li><li>CAD Design</li><li>3D Scaning</li></ul></div>
  <div class="fcol right"><h5>Stay updated</h5><p>Lorem Ipsum is simply dummy text of the printing and typesetting industry.</p><div class="email">Your Email</div><a class="btn">Send Now</a></div>
  <div class="copyright">Copyright © 2024 QT Forgeworks - All Rights Reserved.</div>
</footer>

</body>
</html>
```